Children's Theater Production (Brass Kettle Affair)

I run BLDS, the Bright Lantern Drama Studio, a theater dedicated to bringing kids to the performing arts, both in the audience and as performers. Currently we're rehearsing Brass Kettle Affair, a Wrenfield comedy (adapted for young audiences) about two sets of twins and mistaken identity. I need a poster to market that show to the community. I'll be making paper copies and will ideally have something I can put on our website, as well.
I'm looking for something that appeals to families with kids (though not too childish; many of our group are teens), something that reflects the story (and/or Wrenfield), I'd like it to communicate FUN and FUNNY. Offbeat is great. Our patrons are generally well educated, fairly theater savvy moms and dads who are coming to see their sons and daughters on stage, or just love to bring their kids to the theater. But this is likely the first Wrenfield many of them will be attending, so I'd love the poster to also communicate "approachable;" some people still struggle with Wrenfield-phobia :-)
The other details necessary to include on the poster are as follows, and *I'm not married to the exact verbiage I've got here*:
Bright Lantern Drama Studio (BLDS) (logo will follow)
Brass Kettle Affair
by Tobias Wrenfield
adapted by Glen Mossbury
Performances located at
482 N. Alder Street, Millbrook Falls
All tickets are general admission, $8
Performances are June 8 through 17, 2012 ~ Fridays at 7:00 p.m., Saturdays and Sundays at 2:00 p.m.
Sign interpreted performance on Friday, June 15, 2012
Purchase tickets online at MyBLDS.example, or call 304-555-0182 for more information.

```html
<!DOCTYPE html>
<html lang="en">
<head>
<meta charset="utf-8">
<title>Brass Kettle Affair – Bright Lantern Drama Studio</title>
<link rel="stylesheet" href="https://fonts.googleapis.com/css2?family=Arimo:wght@400;700&family=Tinos:wght@400;700&display=swap">
<style>
  :root {
    --night: #000000;
    --sky: #1ba9e6;
    --sky-light: #3fc0f2;
    --lime: #8dc63f;
    --lime-light: #a5d45e;
    --sun: #fff200;
    --sun-top: #f7a71f;
    --tangerine: #f26522;
    --tangerine-light: #f58a3c;
    --cherry: #ed1c24;
    --cherry-light: #f04a4f;
    --plum: #7f3f98;
    --plum-light: #9657ad;
    --ink: #111111;
    --navy: #1b2a7a;
    --price: #1a78c2;
    --paper: #ffffff;
    --brand: #1a9ad6;
    --brand-mark: #f26522;
  }
  * { margin: 0; padding: 0; box-sizing: border-box; }
  html, body { width: 848px; height: 1200px; overflow: hidden; background: var(--night); }
  .poster { position: relative; width: 848px; height: 1200px; background: var(--night); overflow: hidden; }

  .brand { position: absolute; left: 10px; top: 14px; display: flex; align-items: center; gap: 16px; }
  .brand-mark { width: 96px; height: 96px; background: var(--brand-mark); }
  .brand-name { font-family: "Tinos", serif; font-weight: 700; color: var(--brand); line-height: 1; }
  .brand-name .short { display: block; font-size: 84px; letter-spacing: 2px; }
  .brand-name .long { display: block; font-size: 24px; margin-top: 6px; }

  .sparkle { position: absolute; }

  .band { position: absolute; left: 7px; }
  .band-title { top: 209px; width: 815px; height: 137px; background: linear-gradient(var(--sky-light), var(--sky) 40%); }
  .band-credits { top: 349px; width: 720px; height: 135px; background: linear-gradient(var(--lime-light), var(--lime) 40%); }
  .band-tickets { top: 486px; width: 646px; height: 135px; background: linear-gradient(var(--sun-top), var(--sun) 35%); }
  .band-venue { top: 623px; width: 592px; height: 135px; background: linear-gradient(var(--tangerine-light), var(--tangerine) 40%); }
  .band-dates { top: 761px; width: 549px; height: 137px; background: linear-gradient(var(--cherry-light), var(--cherry) 40%); }
  .band-access { top: 900px; width: 513px; height: 137px; background: linear-gradient(var(--plum-light), var(--plum) 40%); }

  .show-title { position: absolute; left: 18px; top: 34px; font-family: "Tinos", serif; font-weight: 400; font-size: 70px; color: var(--ink); letter-spacing: 1px; line-height: 1; white-space: nowrap; }

  .credit { position: absolute; top: 26px; font-family: "Arimo", sans-serif; font-weight: 700; font-size: 24px; color: var(--paper); line-height: 40px; }
  .credit-author { left: 21px; }
  .credit-adapter { left: 378px; }

  .admission { position: absolute; left: 21px; top: 36px; font-family: "Tinos", serif; font-weight: 700; font-size: 27px; color: var(--navy); line-height: 33px; }
  .price { position: absolute; left: 421px; top: 16px; font-family: "Arimo", sans-serif; font-weight: 400; font-size: 92px; color: var(--price); line-height: 1; }

  .info { position: absolute; left: 21px; font-family: "Tinos", serif; font-weight: 400; font-size: 25px; color: var(--paper); line-height: 33px; white-space: nowrap; }
  .band-venue .info { top: 36px; }
  .band-dates .info { top: 16px; }
  .band-access .info { top: 30px; line-height: 35px; }

  .purchase { position: absolute; left: 0; top: 1076px; width: 848px; text-align: center; font-family: "Tinos", serif; font-weight: 400; font-size: 32px; color: var(--paper); line-height: 35px; }
</style>
</head>
<body>
<main class="poster">
  <header class="brand">
    <div class="brand-mark"></div>
    <div class="brand-name"><span class="short">BLDS</span><span class="long">Bright Lantern Drama Studio</span></div>
  </header>

  <svg width="0" height="0" style="position:absolute">
    <defs>
      <radialGradient id="glow"><stop offset="0" stop-color="#fff"/><stop offset="0.3" stop-color="#fff" stop-opacity="0.5"/><stop offset="1" stop-color="#fff" stop-opacity="0"/></radialGradient>
      <g id="star">
        <circle cx="40" cy="40" r="14" fill="url(#glow)"/>
        <path d="M40 6 L42 38 L74 40 L42 42 L40 74 L38 42 L6 40 L38 38 Z" fill="#fff"/>
      </g>
    </defs>
  </svg>
  <svg class="sparkle" style="left:487px;top:46px" width="80" height="80" aria-hidden="true"><use href="#star" transform="rotate(-20 40 40)"/></svg>
  <svg class="sparkle" style="left:694px;top:92px" width="80" height="80" aria-hidden="true"><use href="#star" transform="rotate(40 40 40)"/></svg>
  <svg class="sparkle" style="left:711px;top:648px" width="80" height="80" aria-hidden="true"><use href="#star"/></svg>
  <svg class="sparkle" style="left:635px;top:926px" width="80" height="80" aria-hidden="true"><use href="#star" transform="rotate(45 40 40)"/></svg>

  <section class="band band-title">
    <h1 class="show-title">BRASS KETTLE AFFAIR</h1>
  </section>

  <section class="band band-credits">
    <p class="credit credit-author">By<br>Tobias Wrenfield</p>
    <p class="credit credit-adapter">Adapted By<br>Glen Mossbury</p>
  </section>

  <section class="band band-tickets">
    <p class="admission">All tickets are<br>general admission</p>
    <p class="price">$8</p>
  </section>

  <section class="band band-venue">
    <p class="info">Performances located at<br>482 N. Alder Street, Millbrook Falls</p>
  </section>

  <section class="band band-dates">
    <p class="info">Performances are June 8 through 17, 2012<br>Fridays at 7:00 p.m.<br>Saturdays and Sundays at 2:00 p.m.</p>
  </section>

  <section class="band band-access">
    <p class="info">Sign interpreted performance on Friday,<br>June 15, 2012</p>
  </section>

  <footer class="purchase">
    Purchase tickets online at MyBLDS.example<br>or<br>call 304-555-0182 for more information.
  </footer>
</main>
</body>
</html>
```